Business cards, letterhead, envelopes & presentation folders
Talbreck Builders "LOGO"
Business cards, letterhead, envelopes & presentation folders - Construction
Creative Brief
Professional
Dennis Oakhurst
Owner
2745 N. Verden Rd. Lodi, CA 95240
talbreck.gc@vornamail.com
WWW.TALBRECK-BUILDERS.COM
CL# 638271
Logo and website address.
talbrekbld talbrekbld
Vepski7q, are you getting my messages? I just need a few revisions to #111 so we can wrap this up. Please check the messages I've been sending you. Thank you!
I uploaded a letterhead design I like.
Draft #13 is my choice for business cards. Still undecided on letter head, envelopes & folders. I'd prefer if the stationary would be a consistent design with the business cards. Thank you

```html
<!DOCTYPE html>
<html lang="en">
<head>
<meta charset="utf-8">
<title>Talbreck Builders — Stationery Set</title>
<link href="https://fonts.googleapis.com/css2?family=Montserrat:wght@400;600;800&display=swap" rel="stylesheet">
<style>
  :root{
    --bg:#e7e7e7;
    --paper:#ffffff;
    --teal:#138a86;
    --dark:#3b3b3b;
    --grey:#9a9a9a;
    --faint:#efefef;
    --ink:#333333;
  }
  html,body{margin:0;padding:0;overflow:hidden;}
  body{width:1200px;height:333px;background:var(--bg);position:relative;font-family:"Montserrat",sans-serif;color:var(--ink);}
  .abs{position:absolute;}
  .sheet{position:absolute;background:var(--paper);box-shadow:0 0 0 .5px #d0d0d0;overflow:hidden;}
  .brand{font-family:"Montserrat",sans-serif;font-weight:800;color:var(--teal);line-height:1;letter-spacing:.04em;white-space:nowrap;display:flex;align-items:center;gap:.35em;}
  .brand .dot{width:.7em;height:.7em;border-radius:50%;background:var(--teal);flex:none;}
  .brand.white{color:#fff;}
  .brand.white .dot{background:#fff;}
  .brand.faint{color:var(--faint);}
  .brand.stack{flex-direction:column;align-items:flex-start;gap:.25em;}
  .wave{position:absolute;left:0;bottom:0;width:100%;}
  .label{position:absolute;top:246px;font-size:8px;color:#333;transform:translateX(-50%);}

  /* business card */
  .card-front .card-brand{position:absolute;left:4px;top:8px;font-size:3.4px;}
  .card-front .person{position:absolute;right:3px;top:9px;text-align:right;font-size:2.4px;font-weight:800;letter-spacing:.04em;white-space:nowrap;}
  .card-front .person small{display:block;font-weight:400;font-size:1.8px;color:#777;margin-top:.5px;}
  .card-front .contacts{position:absolute;left:8px;top:27px;font-size:2px;line-height:3.3px;color:#444;white-space:nowrap;}
  .card-front .contacts span{display:inline-block;width:2px;height:2px;background:var(--teal);margin-right:2px;vertical-align:middle;}
  .card-front .strip{position:absolute;left:0;right:0;bottom:2px;height:2px;background:var(--teal);}
  .card-front .lic{position:absolute;right:0;bottom:0;width:22px;height:4px;background:var(--dark);color:#fff;font-size:1.6px;line-height:4px;text-align:center;}
  .card-back{background:var(--teal);}
  .card-back .web{position:absolute;bottom:2px;width:100%;text-align:center;font-size:1.5px;color:#cfe8e7;letter-spacing:.1em;}

  /* letterhead */
  .letterhead .info{position:absolute;left:10px;top:18px;width:35px;text-align:center;font-size:1.7px;line-height:2.4px;color:#444;}
  .letterhead .info b{font-weight:800;}
  .letterhead .rule{position:absolute;left:14px;top:46px;width:1.6px;height:96px;background:var(--teal);}
  .letterhead .foot{position:absolute;left:7px;bottom:2px;font-size:1.6px;color:#777;}

  /* envelopes */
  .flap{position:absolute;left:0;top:0;width:100%;height:17px;border-radius:0 0 8px 8px;}
  .flap.dark{background:var(--dark);}
  .flap.teal{background:var(--teal);}
  .flap.line{border:.6px solid #e0e0e0;border-top:none;height:13px;width:calc(100% - 2px);}
  .flap .brand{position:absolute;left:50%;top:50%;transform:translate(-50%,-50%);}

  .strip-dark{position:absolute;background:var(--dark);}
</style>
</head>
<body>

<!-- primary name mark -->
<div class="brand stack abs" style="left:40px;top:66px;font-size:15px;">
  <span>TALBRECK</span><span>BUILDERS</span>
</div>

<!-- business card front -->
<div class="sheet card-front" style="left:206px;top:38px;width:82px;height:47px;">
  <div class="brand stack card-brand"><span>TALBRECK</span><span>BUILDERS</span></div>
  <div class="person">DENNIS OAKHURST<small>OWNER</small></div>
  <div class="contacts">
    <div><span></span>209-555-0148</div>
    <div><span></span>209-555-0172</div>
    <div><span></span>talbreck.gc@vornamail.com</div>
    <div><span></span>2745 N. Verden Rd. Lodi, CA 95240</div>
  </div>
  <div class="strip"></div>
  <div class="lic">CL# 638271</div>
</div>

<!-- business card back -->
<div class="sheet card-back" style="left:206px;top:92px;width:82px;height:47px;">
  <div class="brand white" style="position:absolute;left:50%;top:21px;transform:translateX(-50%);font-size:5px;"><span class="dot"></span>TALBRECK BUILDERS</div>
  <div class="web">WWW.TALBRECK-BUILDERS.COM</div>
</div>

<!-- letterhead -->
<div class="sheet letterhead" style="left:41px;top:158px;width:113px;height:148px;">
  <div class="brand" style="position:absolute;left:3px;top:8px;font-size:3.6px;"><span class="dot"></span>TALBRECK</div>
  <div class="info">
    <b>Address:</b><br>2745 N. Verden Rd.<br>Lodi, CA 95240<br>
    <b>Cell Phone No.:</b><br>209-555-0148<br>
    <b>Fax No.:</b><br>209-555-0172<br>
    <b>Email Add.:</b><br>talbreck.gc@vornamail.com
  </div>
  <div class="brand faint" style="position:absolute;left:0;top:62px;font-size:20px;">TALBRECK</div>
  <div class="rule"></div>
  <div class="foot">CL# 638271</div>
</div>

<!-- envelope front -->
<div class="sheet" style="left:188px;top:148px;width:119px;height:51px;">
  <div class="brand" style="position:absolute;left:3px;top:7px;font-size:3.6px;"><span class="dot"></span>TALBRECK</div>
  <svg class="wave" viewBox="0 0 100 100" preserveAspectRatio="none" style="height:100%;">
    <path d="M0 72 C30 100 65 50 100 62" fill="none" stroke="var(--grey)" stroke-width="3"/>
    <path d="M0 77 C30 104 65 56 100 68 L100 100 L0 100Z" fill="var(--teal)"/>
  </svg>
</div>

<!-- envelope backs -->
<div class="sheet" style="left:195px;top:208px;width:118px;height:52px;">
  <div class="flap dark"><div class="brand white" style="font-size:3.4px;">TALBRECK</div></div>
</div>
<div class="sheet" style="left:181px;top:231px;width:118px;height:51px;">
  <div class="flap teal"><div class="brand white" style="font-size:3.4px;">TALBRECK</div></div>
</div>
<div class="sheet" style="left:167px;top:253px;width:118px;height:53px;">
  <div class="flap line"><div class="brand" style="font-size:3.4px;">TALBRECK</div></div>
</div>

<!-- folder: open outside -->
<div class="strip-dark" style="left:328px;top:45px;width:13px;height:194px;"></div>
<div class="strip-dark" style="left:594px;top:45px;width:12px;height:194px;"></div>
<div class="sheet" style="left:341px;top:45px;width:126px;height:194px;">
  <div class="brand faint" style="position:absolute;left:-8px;top:58px;font-size:17px;">TALBRECK</div>
</div>
<div class="sheet" style="left:467px;top:45px;width:127px;height:194px;">
  <div class="brand" style="position:absolute;left:50%;top:64px;transform:translateX(-50%);font-size:9px;"><span class="dot"></span>TALBRECK</div>
  <svg class="wave" viewBox="0 0 100 100" preserveAspectRatio="none" style="height:40px;">
    <path d="M0 10 C35 55 60 -10 100 10" fill="none" stroke="var(--grey)" stroke-width="3"/>
    <path d="M0 18 C35 62 60 0 100 16 L100 100 L0 100Z" fill="var(--teal)"/>
  </svg>
</div>
<svg class="abs" style="left:341px;top:239px;" width="253" height="61" viewBox="0 0 253 61">
  <path d="M0 0 H126 L106 61 H0Z" fill="var(--paper)" stroke="#d6d6d6" stroke-width=".5"/>
  <path d="M126 0 H253 V61 H145Z" fill="var(--teal)"/>
</svg>
<div class="brand" style="position:absolute;left:364px;top:264px;font-size:9px;"><span class="dot"></span>TALBRECK</div>
<div class="brand" style="position:absolute;left:500px;top:258px;font-size:14px;color:#2b9a96;">TALBRECK</div>

<!-- folder: back -->
<div class="sheet" style="left:617px;top:45px;width:126px;height:194px;">
  <div class="brand faint" style="position:absolute;left:-8px;top:58px;font-size:17px;">TALBRECK</div>
</div>
<div class="label" style="left:682px;">Back</div>

<!-- folder: front -->
<div class="sheet" style="left:750px;top:45px;width:127px;height:194px;">
  <div class="brand" style="position:absolute;left:50%;top:64px;transform:translateX(-50%);font-size:9px;"><span class="dot"></span>TALBRECK</div>
  <svg class="wave" viewBox="0 0 100 100" preserveAspectRatio="none" style="height:40px;">
    <path d="M0 10 C35 55 60 -10 100 10" fill="none" stroke="var(--grey)" stroke-width="3"/>
    <path d="M0 18 C35 62 60 0 100 16 L100 100 L0 100Z" fill="var(--teal)"/>
  </svg>
</div>
<div class="label" style="left:814px;">Front</div>

<!-- folder: inside -->
<div class="strip-dark" style="left:885px;top:45px;width:12px;height:134px;"></div>
<div class="strip-dark" style="left:1126px;top:45px;width:12px;height:134px;"></div>
<div class="sheet" style="left:897px;top:45px;width:114px;height:194px;box-shadow:none;"></div>
<div class="sheet" style="left:1011px;top:45px;width:115px;height:194px;box-shadow:-.5px 0 0 #d6d6d6;"></div>
<svg class="abs" style="left:885px;top:179px;" width="253" height="60" viewBox="0 0 253 60">
  <path d="M0 0 H107 L126 60 H0Z" fill="var(--paper)" stroke="#d6d6d6" stroke-width=".5"/>
  <path d="M145 0 H253 V60 H126Z" fill="var(--teal)"/>
</svg>
<div class="brand" style="position:absolute;left:908px;top:205px;font-size:9px;"><span class="dot"></span>TALBRECK</div>
<div class="brand" style="position:absolute;left:1043px;top:208px;font-size:14px;color:#2b9a96;">TALBRECK</div>
<div class="label" style="left:1012px;">Inside</div>

</body>
</html>
```